Coffee bag stamp design for new coffee brand

Stamp design that will be used like a label on a coffee package.
It must be a vector that can be produced as a stamp. Coffee bag is from brown craft paper. I upload image of this bag. Size of design is 80mm x 140mm.
I also uploaded two pictures for inspiration, but I will also appreciate new ideas.

Target Market(s)

Coffee lovers, who love to try new coffee. Also hipsters.

Colors

Designer to choose only greyscale colors for use in the design.

Requirements
Must have
• Some information about coffee must have:
Name: BRAZIL (the biggest font in that design)
Region: Santos
Altitude: 60 – 1200 m.n.m.
Variety: Arabica
Processing: unwashed

```html
<!DOCTYPE html>
<html lang="en">
<head>
<meta charset="utf-8">
<title>Kestrel Coffee – Brazil Santos label</title>
<link rel="stylesheet" href="https://fonts.googleapis.com/css2?family=Montserrat:wght@800&family=Oswald:wght@500&family=Passion+One:wght@400&display=swap">
<style>
  :root {
    --backdrop: #cdc4bb;
    --paper: #d6cec6;
    --ink: #111111;
    --ink-reverse: #d9d1c8;
  }
  html, body {
    margin: 0;
    padding: 0;
    width: 1200px;
    height: 1184px;
    overflow: hidden;
    background: var(--backdrop);
  }
  .stamp-label {
    position: absolute;
    left: 324px;
    top: 90px;
    width: 552px;
    height: 1004px;
  }
  .label-frame { fill: var(--paper); stroke: var(--ink); stroke-width: 4; }
  .ink-band { fill: var(--ink); }
  .brand-mark { fill: none; stroke: var(--ink); stroke-width: 7; }
  .brand-name, .brand-sub, .region, .process {
    font-family: "Montserrat", sans-serif;
    font-weight: 800;
    fill: var(--ink);
  }
  .origin {
    font-family: "Passion One", sans-serif;
    fill: var(--ink-reverse);
  }
  .process { fill: var(--ink-reverse); }
  .rule { stroke: var(--ink); stroke-width: 2.5; }
  .dot-rule { stroke: var(--ink); stroke-width: 3.5; stroke-linecap: round; stroke-dasharray: 0 8; }
  .spec {
    font-family: "Oswald", sans-serif;
    font-weight: 500;
    font-size: 29px;
    fill: var(--ink);
  }
</style>
</head>
<body>
  <svg class="stamp-label" viewBox="0 0 552 1004" xmlns="http://www.w3.org/2000/svg">
    <!-- outline with arched top -->
    <path class="label-frame" d="M2,1002 L2,232 L46,232 L46,160 A229.5,158 0 0 1 505,160 L505,232 L550,232 L550,1002 Z"/>

    <!-- brand -->
    <circle class="brand-mark" cx="276" cy="170" r="58"/>
    <text class="brand-name" x="276" y="304" text-anchor="middle" font-size="72" textLength="416" lengthAdjust="spacingAndGlyphs">KESTREL</text>
    <text class="brand-sub" x="276" y="360" text-anchor="middle" font-size="50" textLength="211" lengthAdjust="spacingAndGlyphs">COFFEE</text>

    <!-- origin band -->
    <rect class="ink-band" x="2" y="457" width="548" height="174"/>
    <text class="origin" x="276" y="602" text-anchor="middle" font-size="176" textLength="510" lengthAdjust="spacingAndGlyphs">BRAZIL</text>

    <!-- region -->
    <line class="rule" x1="52" y1="664" x2="167" y2="664"/>
    <line class="rule" x1="81" y1="673" x2="167" y2="673"/>
    <line class="rule" x1="383" y1="664" x2="499" y2="664"/>
    <line class="rule" x1="383" y1="673" x2="471" y2="673"/>
    <text class="region" x="276" y="681" text-anchor="middle" font-size="36" textLength="184" lengthAdjust="spacingAndGlyphs">SANTOS</text>

    <!-- details -->
    <line class="dot-rule" x1="27" y1="729" x2="527" y2="729"/>
    <line class="dot-rule" x1="227" y1="751" x2="227" y2="847"/>
    <text class="spec" x="66" y="789">Altitude:</text>
    <text class="spec" x="66" y="830">Variety:</text>
    <text class="spec" x="281" y="789">60 - 1200 m.n.m.</text>
    <text class="spec" x="281" y="830">Arabica</text>
    <line class="dot-rule" x1="27" y1="870" x2="527" y2="870"/>

    <!-- processing band -->
    <rect class="ink-band" x="2" y="898" width="548" height="104"/>
    <text class="process" x="276" y="975" text-anchor="middle" font-size="76" textLength="459" lengthAdjust="spacingAndGlyphs">UNWASHED</text>
  </svg>
</body>
</html>
```